Thankyou post card for our customers

we would like to have a design for a post card that we would like to send to our customers once they have hired from us to say thankyou and to offer them a discount on there next hire.

our business is called Wandering Gum Caravan Rentals.
we hire our camper trailers and are based in Australia so alot of our customers go to the outback bush, beach etc with our campers.
the post card dimesions are
Full Bleed Size

213 x 98 mm
2517 x 1158 pixels

Document Trim Size

210 x 95 mm
2481 x 1122 pixels

I want 4 lines for the name and address on the right have side of the post card (like normal post cards have

Industry/Entity Type

Business

Requirements
Must have
• we want it to be double sided so a Design on front and back of post card
I have attached our logo and some other things we have used in previous business material up to you if you want to use what I have uploaded

please note the logo with sunset I have attached I do not want the round logo used just wanted to show you how great the sunset looks we have changed our logo to just be the Wandering Gum Caravan Rentals but wouldnt mind if you used a sunset like this on the whole of the card? but not limited to that.

front of card:
our logo on front page (which is just the Wandering Gum Caravan Rentals attachement WGCR1)
and our details:
P: 0491 326 715
W: www.wanderinggumcaravanrentals.com.au
E:info@wanderinggumcaravanrentals.com.au

and the following to be on the front of the post card:

Dear Fellow Campers,
We hope you have arrived home safely, and are rested and relaxed from your trip away. It was our pleasure to have you hire one of our campers and would like to thankyou for your support, we trust you enjoyed glamping and would like to think you would hire from us again. to show our appreciation we would like to offer you a 20% discount on any minimum 7 day hire over the next 6 months. we look forward to hearing from you again soon.
sincerely,
Graham & Leonie

offer not valid in peak period or in conjuction with any other offer

Full Bleed Size

213 x 98 mm
2517 x 1158 pixels

Document Trim Size

210 x 95 mm
2481 x 1122 pixels

Back of Card:

I want "Thankyou" written at top and then how ever else you design it

```html
<!DOCTYPE html>
<html lang="en">
<head>
<meta charset="utf-8">
<title>Wandering Gum Caravan Rentals – Thank You Postcard</title>
<link rel="stylesheet" href="https://fonts.googleapis.com/css2?family=Oswald:wght@600;700&family=Cormorant+Garamond:wght@500&family=Cardo&family=Special+Elite&family=Arimo:ital,wght@0,400;0,700;1,400&display=swap">
<style>
  :root {
    --page: #ffffff;
    --ink: #1a1a1a;
    --red: #e3101b;
    --line: #b9bcbf;
    --white-soft: rgba(255,255,255,0.82);
    --shadow: rgba(0,0,0,0.28);
  }
  * { box-sizing: border-box; margin: 0; padding: 0; }
  html, body { width: 1200px; height: 1114px; overflow: hidden; background: var(--page); }
  .canvas { position: relative; width: 1200px; height: 1114px; }

  .card { position: absolute; overflow: hidden; box-shadow: 0 2px 6px var(--shadow); }
  .card--front { left: 118px; top: 86px; width: 952px; height: 430px; }
  .card--back  { left: 118px; top: 590px; width: 960px; height: 436px; }

  .scene { position: absolute; inset: 0; }
  .scene--sunset-track {
    background:
      radial-gradient(circle at 45% 8%, rgba(255,250,200,1) 0, rgba(255,205,90,0.85) 6%, rgba(240,160,40,0) 30%),
      linear-gradient(180deg, #c98b2c 0%, #d9a23d 10%, #8f9a3c 24%, #6f8d3a 40%, #86995a 55%, #b9b39a 66%, #e9e8e3 78%, #f6f6f4 100%);
  }
  .scene--dune-sky {
    background:
      radial-gradient(ellipse at 30% 10%, rgba(255,255,255,0.85) 0, rgba(255,255,255,0) 35%),
      radial-gradient(ellipse at 85% 70%, rgba(120,140,60,0.9) 0, rgba(140,150,80,0) 40%),
      linear-gradient(180deg, #3f73b6 0%, #6f9bd0 30%, #b8cde4 50%, #dcdfd6 72%, #ece8dd 85%, #f3f1ec 100%);
  }
  .paper-fade {
    position: absolute; left: 0; right: 0; bottom: 0; height: 210px;
    background: linear-gradient(180deg, rgba(255,255,255,0) 0%, rgba(255,255,255,0.75) 30%, rgba(255,255,255,0.92) 100%);
  }

  .offer-badge {
    position: absolute; left: 20px; top: 104px; width: 316px; height: 82px;
    background: var(--page); border-radius: 10px; transform: rotate(-3deg);
    display: flex; align-items: center; padding-left: 18px; gap: 10px;
  }
  .offer-badge__value { font: 700 66px/1 "Oswald", sans-serif; color: var(--red); letter-spacing: -2px; white-space: nowrap; }
  .offer-badge__text { font: 21px/1.1 "Special Elite", serif; color: var(--red); white-space: nowrap; }

  .stamp-box {
    position: absolute; left: 826px; top: 35px; width: 87px; height: 100px;
    border: 1px solid rgba(255,255,255,0.9); color: #fff;
    font: 12px/1.9 "Arimo", sans-serif; text-align: center; padding-top: 28px;
  }

  .brand { position: absolute; }
  .brand__name { font: 600 26px/1.05 "Oswald", sans-serif; color: var(--ink); text-transform: uppercase; letter-spacing: 0.5px; }
  .front-brand { left: 44px; top: 262px; }

  .contact { list-style: none; margin-top: 8px; }
  .contact li { display: flex; align-items: center; gap: 7px; font: 700 14.5px/20px "Arimo", sans-serif; color: var(--ink); white-space: nowrap; }
  .contact svg { width: 13px; height: 13px; flex: none; }

  .address-lines { position: absolute; left: 506px; top: 254px; }
  .address-lines span { display: block; height: 1px; background: var(--line); width: 396px; margin-bottom: 40px; }
  .address-lines span:last-child { width: 176px; }

  .postcode { position: absolute; left: 705px; top: 356px; display: flex; gap: 13px; }
  .postcode span { width: 42px; height: 43px; background: rgba(255,255,255,0.9); border: 1px solid #d6d6d6; }

  .thanks-heading {
    position: absolute; left: 138px; top: 14px;
    font: 92px/1 "Cardo", serif; color: rgba(255,255,255,0.42); letter-spacing: 2px; white-space: nowrap;
  }
  .letter-panel {
    position: absolute; left: 0; top: 150px; width: 500px; height: 286px;
    background: linear-gradient(90deg, rgba(255,255,255,0.55), var(--white-soft) 10%, var(--white-soft) 88%, rgba(255,255,255,0.3));
  }
  .letter {
    position: absolute; left: 44px; top: 170px; width: 432px;
    font: 500 16.5px/21.4px "Cormorant Garamond", serif; color: var(--ink); text-align: justify;
  }
  .letter .highlight { color: var(--red); }
  .fine-print {
    position: absolute; left: 42px; top: 408px;
    font: italic 11px/1 "Arimo", sans-serif; color: #333; white-space: nowrap;
  }
  .back-brand { left: 640px; top: 262px; }
  .back-brand .brand__name { font-size: 24px; }
  .back-brand .contact li { font-size: 12px; line-height: 18px; }
</style>
</head>
<body>
<div class="canvas">

  <section class="card card--front">
    <div class="scene scene--sunset-track" role="img" aria-label="Photograph of a dirt track winding through green fields toward a low setting sun"></div>
    <div class="paper-fade"></div>

    <div class="offer-badge">
      <span class="offer-badge__value">20%</span>
      <span class="offer-badge__text">OFF ON YOUR<br>NEXT HIRE !</span>
    </div>

    <div class="stamp-box">stamp<br>here</div>

    <div class="brand front-brand">
      <p class="brand__name">Wandering Gum<br>Caravan Rentals</p>
      <ul class="contact">
        <li><svg viewBox="0 0 16 16"><path fill="#e3101b" d="M3.5 1l2.5 3-1.5 2c1 2 3 4 5 5l2-1.5 3 2.5-1.5 2.5C7 15 1 9 1 2.5z"/></svg>0491 326 715</li>
        <li><svg viewBox="0 0 16 16"><g fill="none" stroke="#e3101b" stroke-width="1.5"><circle cx="8" cy="8" r="6.5"/><ellipse cx="8" cy="8" rx="3" ry="6.5"/><path d="M1.5 8h13"/></g></svg>www.wanderinggumcaravanrentals.com.au</li>
        <li><svg viewBox="0 0 16 16"><rect x="1" y="3" width="14" height="10" fill="#e3101b"/><path d="M1.5 3.5L8 9l6.5-5.5" fill="none" stroke="#fff" stroke-width="1.3"/></svg>info@wanderinggumcaravanrentals.com.au</li>
      </ul>
    </div>

    <div class="address-lines"><span></span><span></span><span></span><span></span></div>
    <div class="postcode"><span></span><span></span><span></span><span></span></div>
  </section>

  <section class="card card--back">
    <div class="scene scene--dune-sky" role="img" aria-label="Photograph of coastal dune grass against a blue sky with white clouds over pale sand"></div>
    <p class="thanks-heading">Thank you!</p>
    <div class="letter-panel"></div>

    <div class="letter">
      <p>Dear Fellow Campers,</p>
      <p>We hope you have arrived home safely, and are rested and relaxed from your trip away. It was our pleasure to have you hire one of our campers and would like to thankyou for your support, we trust you enjoyed glamping and would like to think you would hire from us again. To show our appreciation we would like to offer you a <span class="highlight">20% discount</span> on any minimum 7 day hire over the next 6 months. We look forward to hearing from you again soon.</p>
      <p>Sincerely, Graham &amp; Leonie</p>
    </div>
    <p class="fine-print">*Not valid in peak periods and can not be used in conjunction with any other offer.</p>

    <div class="brand back-brand">
      <p class="brand__name">Wandering Gum<br>Caravan Rentals</p>
      <ul class="contact">
        <li><svg viewBox="0 0 16 16"><path fill="#e3101b" d="M3.5 1l2.5 3-1.5 2c1 2 3 4 5 5l2-1.5 3 2.5-1.5 2.5C7 15 1 9 1 2.5z"/></svg>0491 326 715</li>
        <li><svg viewBox="0 0 16 16"><g fill="none" stroke="#e3101b" stroke-width="1.5"><circle cx="8" cy="8" r="6.5"/><ellipse cx="8" cy="8" rx="3" ry="6.5"/><path d="M1.5 8h13"/></g></svg>www.wanderinggumcaravanrentals.com.au</li>
        <li><svg viewBox="0 0 16 16"><rect x="1" y="3" width="14" height="10" fill="#e3101b"/><path d="M1.5 3.5L8 9l6.5-5.5" fill="none" stroke="#fff" stroke-width="1.3"/></svg>info@wanderinggumcaravanrentals.com.au</li>
      </ul>
    </div>
  </section>

</div>
</body>
</html>
```